New Jar Label for Manuka Honey Company!

Hine Roa Honey, a Manuka Honey company from New Zealand is looking for a fresh & engaging label for our manuka honey jars.

Attached are some examples of label designs that we like, feel free to use the language/copy on these labels for inspiration/content/copy, but feel free to add your own creative spin if you have a great design idea!

LABEL DIMENSIONS: 1654mmx532mm

Label Must Include:
- MGO rating
- Made (or) Product of New Zealand
- Manuka Honey (can add extra text similar to attached examples)

Label Can Include:
- Badges: raw food, non gmo, bpa free, gluten free, halal etc
- anything you feel is appropriate

You can change the color of the logo(s) to Black, White, Silver or Gold.

Can you please include a mockup of your label design(s) on the supplied "Jar Mockup File". You can change the scene of the mockup if you like.

UPDATE:

Have decided on bee logo so please bo longer use the mountain logo for label mockups. Design(s) will need multiple color variations to represent the other MGO ratings, flavor combos and other honey types, other than manuka.

• Provide multiple designs for each honey type
Manuka Design
Spring Honey Design
MGO 100-1000 Design(s)
Wildflower Honey Design
Flavor Combo Honey Design

```html
<!DOCTYPE html>
<html lang="en">
<head>
<meta charset="utf-8">
<title>Hine Roa Honey – Manuka Honey Label</title>
<link href="https://fonts.googleapis.com/css2?family=Montserrat:wght@800&family=Roboto+Condensed:wght@400&display=swap" rel="stylesheet">
<style>
  :root {
    --page-bg: #ffffff;
    --label-left: #8c7062;
    --label-mid: #58311d;
    --label-right: #6b4a46;
    --gold: #dcb83c;
    --white: #ffffff;
    --pill-light: #f6dc6c;
    --pill-deep: #f0c11a;
    --ink: #2b2b2b;
    --badge-green: #27b24f;
    --badge-ring: #1d7d3a;
    --comb-gold: #f2c12e;
    --comb-dark: #5a4038;
  }
  html, body {
    margin: 0;
    width: 1200px;
    height: 1200px;
    overflow: hidden;
    background: var(--page-bg);
  }
  .canvas {
    width: 1200px;
    height: 1200px;
    display: flex;
    align-items: center;
    justify-content: center;
  }
  .jar-label {
    width: 1100px;
    height: 662px;
    display: block;
  }
  .brand-name {
    font-family: "Roboto Condensed", sans-serif;
    font-weight: 400;
    fill: var(--white);
  }
  .origin-line {
    font-family: "Roboto Condensed", sans-serif;
    fill: var(--gold);
  }
  .product-title {
    font-family: "Roboto Condensed", sans-serif;
    fill: var(--white);
  }
  .mgo-number {
    font-family: "Montserrat", sans-serif;
    font-weight: 800;
    fill: var(--ink);
  }
  .mgo-unit {
    font-family: "Roboto Condensed", sans-serif;
    fill: var(--ink);
  }
</style>
</head>
<body>
<main class="canvas">
  <svg class="jar-label" viewBox="0 0 1100 662" xmlns="http://www.w3.org/2000/svg">
    <defs>
      <linearGradient id="labelBase" x1="0" y1="0" x2="1" y2="0">
        <stop offset="0" stop-color="var(--label-left)"/>
        <stop offset="0.25" stop-color="#7a5a4b"/>
        <stop offset="0.48" stop-color="var(--label-mid)"/>
        <stop offset="0.75" stop-color="#5e3a2c"/>
        <stop offset="1" stop-color="var(--label-right)"/>
      </linearGradient>
      <linearGradient id="labelShade" x1="0" y1="0" x2="0" y2="1">
        <stop offset="0.55" stop-color="#000" stop-opacity="0"/>
        <stop offset="1" stop-color="#1a0a06" stop-opacity="0.45"/>
      </linearGradient>
      <linearGradient id="pillFill" x1="0" y1="0" x2="1" y2="0">
        <stop offset="0" stop-color="var(--pill-light)"/>
        <stop offset="1" stop-color="var(--pill-deep)"/>
      </linearGradient>
      <linearGradient id="combFill" x1="0" y1="0" x2="1" y2="0">
        <stop offset="0" stop-color="var(--comb-dark)"/>
        <stop offset="0.45" stop-color="#b8892a"/>
        <stop offset="1" stop-color="var(--comb-gold)"/>
      </linearGradient>
    </defs>

    <g class="label-background">
      <rect width="1100" height="662" fill="url(#labelBase)"/>
      <rect width="1100" height="662" fill="url(#labelShade)"/>
    </g>

    <text class="brand-name" x="550" y="128" text-anchor="middle" font-size="40">Hine Roa Honey</text>

    <text class="origin-line" x="550" y="240" text-anchor="middle" font-size="56" textLength="482" lengthAdjust="spacingAndGlyphs">Product of New Zealand</text>

    <text class="product-title" x="550" y="382" text-anchor="middle" font-size="140" textLength="710" lengthAdjust="spacingAndGlyphs">MANUKA HONEY</text>

    <g class="mgo-rating">
      <rect x="234" y="439" width="636" height="141" rx="70.5" fill="url(#pillFill)"/>
      <text class="mgo-number" x="286" y="552" font-size="118" textLength="277" lengthAdjust="spacingAndGlyphs">829+</text>
      <text class="mgo-unit" x="582" y="548" font-size="92" textLength="138" lengthAdjust="spacingAndGlyphs">MGO</text>
      <g class="certification-badge">
        <circle cx="801" cy="507" r="64" fill="var(--badge-ring)"/>
        <circle cx="801" cy="507" r="56" fill="var(--badge-green)"/>
      </g>
    </g>

    <rect class="honeycomb-art" x="987" y="0" width="113" height="662" fill="url(#combFill)" role="img" aria-label="Golden honeycomb illustration with bees"/>
  </svg>
</main>
</body>
</html>
```